Mental Health

QRT HAVEN
Behavioral Health
4172 W. Pell St. Mesa, AZ 85219
Gwendolyn (480)555-0142 / Omar 480-555-0187

Email: QRTHaven@Mailvex.example
Newly Remodeled & Spacious
g Staff
Registered Nurses
Licensed Independent &
Professional Substance &
Abuse Counselors
Behavioral Health Techs
Certified Caregivers
Behavioral Health &
Substance Abuse Professionals

To Refer a Patient
About Us
QRT Haven is a Fully Staffed Behavioral
Health Residential Facility, providing
treatment plans for adults suffering
with various Behavioral Health and
Substance Abuse disorders, while living
in a nice safe, clean and supportive
environment. Our home offers clients the
ability to learn the necessary skills to
help clients adapt, build self confidence
as well as independence, with the goal
of reducing the probability of a future
crisis or possible relapse. We offer
counseling programs, consisting of a
variety of addiction and recovery support
groups, independent living, coping and
social skills groups, as well as assisting
clients with using tools to create a resume
to help obtain employment and so much
more. We are committed to teaching
self management care and allowing
clients to understand how to utilize the
resources, skills and tools available for
long term success by providing superior
quality, all-inclusive living arrangements
and treatment options.

Thank you for your patience while I update the final content needed for us to make the final decision this week.

```html
<!DOCTYPE html>
<html lang="en">
<head>
<meta charset="utf-8">
<title>QRT Haven – Business Card</title>
<link rel="stylesheet" href="https://fonts.googleapis.com/css2?family=Arimo:wght@400;700&family=Montserrat:wght@600;700&display=swap">
<style>
  :root {
    --brand-blue: #0a6fbc;
    --brand-green: #6db33f;
    --brand-orange: #f47b2a;
    --brand-teal: #2a8a8e;
    --paper: #ffffff;
    --ink-gray: #4a4a4a;
    --backdrop: #1c1c1c;
  }
  * { margin: 0; padding: 0; box-sizing: border-box; }
  html, body { width: 1200px; height: 1015px; overflow: hidden; }
  body {
    background: var(--backdrop);
    font-family: "Arimo", Arial, sans-serif;
    display: flex;
    flex-direction: column;
    align-items: center;
    justify-content: center;
    gap: 15px;
  }
  .card {
    position: relative;
    width: 840px;
    height: 480px;
    overflow: hidden;
    background: var(--paper);
    box-shadow: 0 6px 18px rgba(0,0,0,.5);
  }
  .card-art { position: absolute; inset: 0; width: 100%; height: 100%; }

  /* Services side */
  .service-list {
    position: absolute;
    list-style: none;
    color: var(--paper);
    font-size: 24px;
    line-height: 30px;
  }
  .service-list li::before {
    content: "";
    display: inline-block;
    width: 9px; height: 9px;
    border-radius: 50%;
    background: var(--paper);
    margin-right: 10px;
    vertical-align: middle;
  }
  .service-list--left { left: 40px; top: 58px; }
  .service-list--right { left: 450px; top: 24px; }

  .wordmark {
    position: absolute;
    display: flex;
    align-items: center;
    gap: 16px;
    color: var(--brand-blue);
    font-weight: 400;
    font-size: 52px;
    line-height: 1;
    letter-spacing: 2px;
    white-space: nowrap;
  }
  .wordmark__dot {
    width: 64px; height: 64px;
    border-radius: 50%;
    background: var(--brand-green);
  }
  .services .wordmark { right: 40px; top: 325px; }

  /* Contact side */
  .contacts {
    position: absolute;
    right: 55px;
    top: 28px;
    text-align: right;
  }
  .contact__name {
    font-family: "Montserrat", Arial, sans-serif;
    font-weight: 700;
    font-size: 30px;
    line-height: 36px;
    color: var(--brand-blue);
    text-transform: uppercase;
  }
  .contact__phone { font-size: 23px; line-height: 28px; color: var(--ink-gray); margin-bottom: 10px; }
  .contact__label { color: var(--brand-green); font-weight: 700; }

  .contact .wordmark { left: 55px; top: 190px; }

  .address-block {
    position: absolute;
    right: 45px;
    bottom: 30px;
    text-align: right;
    color: var(--paper);
    font-size: 21px;
    line-height: 27px;
  }
  .address-block__email { margin-bottom: 14px; }
  .address-block__company { font-weight: 700; }
</style>
</head>
<body>

  <section class="card services">
    <svg class="card-art" viewBox="0 0 840 480" aria-hidden="true">
      <rect width="840" height="480" fill="var(--brand-blue)"/>
      <path d="M0 430 C 150 428 260 400 330 330 C 420 240 520 220 840 210 L840 480 L0 480 Z" fill="var(--paper)"/>
      <path d="M0 442 C 150 440 260 412 330 342 C 420 252 520 232 840 222" fill="none" stroke="var(--brand-green)" stroke-width="7"/>
      <path d="M0 455 C 150 453 260 425 330 355 C 420 265 520 245 840 235" fill="none" stroke="var(--brand-orange)" stroke-width="7"/>
    </svg>
    <ul class="service-list service-list--left">
      <li>Newly Remodeled &amp; Spacious</li>
      <li>General Staff</li>
      <li>Registered Nurses</li>
      <li>Licensed Independent</li>
      <li>Professional Substance</li>
    </ul>
    <ul class="service-list service-list--right">
      <li>Abuse Counselors</li>
      <li>Behavioral Health Techs</li>
      <li>Certified Caregivers</li>
      <li>Behavioral Health</li>
      <li>Substance Abuse Professionals</li>
    </ul>
    <div class="wordmark"><span class="wordmark__dot"></span>QRT HAVEN</div>
  </section>

  <section class="card contact">
    <svg class="card-art" viewBox="0 0 840 480" aria-hidden="true">
      <defs>
        <linearGradient id="stripe-upper" x1="0" x2="1">
          <stop offset="0" stop-color="var(--brand-orange)"/>
          <stop offset=".55" stop-color="var(--brand-orange)"/>
          <stop offset="1" stop-color="var(--brand-green)"/>
        </linearGradient>
        <linearGradient id="stripe-lower" x1="0" x2="1">
          <stop offset="0" stop-color="var(--brand-blue)"/>
          <stop offset=".5" stop-color="var(--brand-teal)"/>
          <stop offset="1" stop-color="var(--brand-green)"/>
        </linearGradient>
      </defs>
      <rect width="840" height="480" fill="var(--paper)"/>
      <path d="M0 418 C 210 440 340 420 460 320 C 570 230 660 235 840 232 L840 480 L0 480 Z" fill="var(--brand-blue)"/>
      <path d="M0 392 C 210 414 340 394 460 294 C 570 204 660 209 840 206" fill="none" stroke="url(#stripe-upper)" stroke-width="7"/>
      <path d="M0 405 C 210 427 340 407 460 307 C 570 217 660 222 840 219" fill="none" stroke="url(#stripe-lower)" stroke-width="7"/>
    </svg>
    <div class="wordmark"><span class="wordmark__dot"></span>QRT HAVEN</div>
    <div class="contacts">
      <p class="contact__name">Gwendolyn</p>
      <p class="contact__phone"><span class="contact__label">P:</span> (480)555-0142</p>
      <p class="contact__name">Omar</p>
      <p class="contact__phone"><span class="contact__label">P:</span> 480-555-0187</p>
    </div>
    <div class="address-block">
      <p class="address-block__email">QRTHaven@Mailvex.example</p>
      <p class="address-block__company">QRT HAVEN</p>
      <p>Behavioral Health</p>
      <p>4172 W. Pell St. Mesa, AZ 85219</p>
    </div>
  </section>

</body>
</html>
```